Online Psychiatry business - Business Card

I need a business card design. The target audience is busy professionals of any field (this therapy appeals best to 24-35 year olds). It involves psychiatry by tele-medicine (or video-conference). Nothing on it should be a giveaway that it's about mental health. Professional design with silver or gold as the primary colors appeals to me. The card must be as simple and as uncluttered as possible. Some color and flowing design on the edge of the card appeals to me.
CrestLumaCareNet.com should probably appear in the center of the card and stand out, i.e. bold lettering, and easy to read, no cursive, but Ariel Black. Some where below this, should appear "Too Busy to Take Care of Yourself? Think again." Since this isn't office based, I don't think an office address is necessary and limits clutter.
Information that does need to appear is my name: Gerald Mewkinson, MD
General phone number: 618-472-9086. I'm hoping to get an 24-hour answering service soon so leave a little room for this. In addition I want to include two email addresses:
CrestLumaCareNet@mailvora.com and CrestLumaCare247@mailvora.com
Updates

I like the designs. I would like someone to put the website in bold in the center

 as most have been doing with a smaller font reminder nearby saying "No time" etc.
but I'd like to put my name down in the corner with the rest of the contact material.
Black print against a white or grey background appeals to me, with darker silver artwork near the sides (simple abstract, like wavy lines or something you can one up with that works. 
thanks

I ve tried to provide as much feedback as possible given my time limits, so if you have extra questions, please feel free to email. I tried to attach a file of a business card I really like but make be difficult to actually manufacture. I'm going to send you a link to the photo. The card has a pull tab. There is not much information on the outside. In fact, if you were to design the outside, I would just print : Too Busy to Take Care of Yourself? Think Again.

When you pull the tab the remaining information is on the bottom half of the card. Please don't use the color pink!!!!
http://www.printfolkgallery.net/2009/05/100-really-creative-business-cards/
It is the 39th photo on the list, about 2/3ds of the way down the page. It is titled: Ruvelinkiste

#7 and #16 have an appeal to me, except for the dot patterns
Hope this helps

I'm running out of time and energy. I 've been trying to give do down the list and give  individual feedback but I won't be able to do that anymore.

So if you have any specific questions, write me, and again thank you for all your effort!!

I know i received your files, including your zip files, Tolkra,

but Milos, did you send me the files including ZIP on project 5139624?
thanks

Target Market(s)

Working professionals and executive, attorneys, etc.

Industry/Entity Type

Business

Logo Text

Don't Have Time to Take Care of Yourself? Think Again.

Logo styles of interest
Pictorial/Combination Logo
Wordmark Logo
Font styles to use
Other font styles liked:
• Ariel Black appeals to me the most

Requirements
Must have
• Want to emphasize that the website must be obvious, easily found (The CrestLumaCareNet.com)
For that reason i'd like the card to be white, and minimal decoration on one or both sides just to add some style and color
Nice to have
• A Very uncluttered, elegant design, and something that makes it stick in your head-doesn't everyone want the last?
Should not have
• Nothing on the card that give it away that this is about psychiatry, such as brain or other symbol, but also nothing that gives it away as a medical business, such as a stethoscope or red cross or anything.

```html
<!DOCTYPE html>
<html lang="en">
<head>
<meta charset="utf-8">
<title>CrestLumaCareNet – Business Card</title>
<link href="https://fonts.googleapis.com/css2?family=Questrial&display=swap" rel="stylesheet">
<style>
  :root{
    --sheet-light:#fbfbfa;
    --sheet-edge:#e6e5e2;
    --side-label:#e7e6e3;
    --divider:#e4e3e0;
    --metal-dark:#1f2121;
    --metal-mid:#4a4c4c;
    --gold:#a68d4b;
    --ink-dark:#2a2b2b;
    --url-light:#b9bcbc;
    --silver-light:#f6f7f7;
    --silver-mid:#d5d8d9;
    --silver-dark:#bfc3c5;
    --ink:#1e1e1e;
    --bronze:#6e5524;
  }
  *{margin:0;padding:0;box-sizing:border-box}
  html,body{width:1200px;height:1000px;overflow:hidden}
  body{
    position:relative;
    font-family:"Questrial",sans-serif;
    background:radial-gradient(ellipse 70% 60% at 50% 45%,var(--sheet-light) 0%,#f3f2f0 65%,var(--sheet-edge) 100%);
  }
  .side-label{
    position:absolute;left:0;width:222px;text-align:right;
    font-size:34px;font-weight:700;letter-spacing:1px;color:var(--side-label);
    font-family:Arial,Helvetica,sans-serif;
  }
  .side-label--front{top:248px}
  .side-label--back{top:716px}
  .divider{position:absolute;left:265px;width:9px;background:var(--divider)}
  .divider--front{top:61px;height:418px}
  .divider--back{top:517px;height:418px}

  .card{position:absolute;left:314px;width:718px;height:418px;overflow:hidden}

  /* front */
  .card--front{
    top:61px;
    background:
      repeating-linear-gradient(0deg,rgba(255,255,255,.025) 0 1px,transparent 1px 3px,rgba(0,0,0,.05) 3px 4px),
      radial-gradient(ellipse 45% 55% at 50% 45%,rgba(120,122,122,.55),transparent 75%),
      linear-gradient(180deg,var(--metal-dark) 0%,var(--metal-mid) 50%,var(--metal-dark) 100%);
  }
  .tagline-band{
    position:absolute;left:50px;top:133px;width:620px;height:32px;
    background:linear-gradient(90deg,transparent 0%,var(--gold) 14%,#b39a57 50%,var(--gold) 86%,transparent 100%);
  }
  .tagline{
    position:absolute;left:0;right:0;top:139px;text-align:center;
    font-size:19px;letter-spacing:2.6px;color:var(--ink-dark);padding-left:4px;
  }
  .headline{
    position:absolute;left:0;right:0;top:166px;text-align:center;
    font-size:74px;letter-spacing:1px;line-height:1;color:#303232;padding-left:22px;
    text-shadow:1px 1px 0 rgba(255,255,255,.22),-1px -1px 0 rgba(0,0,0,.7);
  }
  .front-url{
    position:absolute;left:0;right:0;top:251px;text-align:center;
    font-size:20px;letter-spacing:3.4px;color:var(--url-light);padding-left:12px;
  }

  /* back */
  .card--back{
    top:517px;
    background:
      repeating-linear-gradient(0deg,rgba(255,255,255,.25) 0 1px,transparent 1px 3px),
      linear-gradient(180deg,var(--silver-dark) 0%,#e3e5e6 25%,var(--silver-light) 48%,var(--silver-mid) 80%,#c9cccd 100%);
  }
  .back-swoosh{position:absolute;inset:0}
  .back-title{position:absolute;left:33px;top:42px;font-size:30px;color:var(--ink);letter-spacing:.3px}
  .back-url{position:absolute;left:33px;top:77px;font-size:22px;color:var(--bronze)}
  .emails{position:absolute;left:33px;top:150px;font-size:21px;line-height:31px;color:var(--bronze)}
  .emails .label{color:var(--ink)}
  .emails .indent{padding-left:23px}
  .phones{position:absolute;right:37px;top:300px;font-size:22px;color:var(--ink);text-align:right}
  .phone-row{display:flex;align-items:center;justify-content:flex-end;height:53px;gap:12px}
</style>
</head>
<body>
  <div class="side-label side-label--front">FRONT</div>
  <div class="divider divider--front"></div>
  <div class="side-label side-label--back">BACK</div>
  <div class="divider divider--back"></div>

  <section class="card card--front">
    <div class="tagline-band"></div>
    <p class="tagline">NO TIME TO TAKE CARE OF YOURSELF?</p>
    <h1 class="headline">THINK AGAIN</h1>
    <p class="front-url">www.crestlumacarenet.com</p>
  </section>

  <section class="card card--back">
    <svg class="back-swoosh" viewBox="0 0 718 418" preserveAspectRatio="none" aria-hidden="true">
      <path d="M0 370 C220 300 480 210 718 130 L718 418 L0 418 Z" fill="rgba(255,255,255,.28)"/>
      <path d="M0 370 C220 300 480 210 718 130" fill="none" stroke="rgba(255,255,255,.6)" stroke-width="1.5"/>
    </svg>
    <h2 class="back-title">YOUR TIME IS VALUABLE</h2>
    <p class="back-url">www.crestlumacarenet.com</p>
    <div class="emails">
      <div><span class="label">E:</span> CrestLumaCareNet@mailvora.com</div>
      <div class="indent">CrestLumaCare247@mailvora.com</div>
    </div>
    <div class="phones">
      <div class="phone-row">
        <svg width="26" height="30" viewBox="0 0 24 28" aria-hidden="true">
          <path d="M6 2 L10 8 L8 11 C9 15 11 18 14 20 L17 18 L22 23 L19 26 C10 25 3 16 2 6 Z" fill="var(--ink)"/>
        </svg>
        <span>618.472.9086</span>
      </div>
      <div class="phone-row">
        <svg width="52" height="40" viewBox="0 0 52 40" aria-hidden="true">
          <circle cx="30" cy="20" r="16" fill="none" stroke="var(--ink)" stroke-width="2" stroke-dasharray="60 6"/>
          <path d="M6 8 L10 13 L8 16 C9 20 11 23 14 25 L17 23 L21 28 L18 31 C10 30 3 22 2 12 Z" fill="var(--ink)"/>
          <text x="30" y="24" text-anchor="middle" font-family="Arial,sans-serif" font-weight="700" font-size="12" fill="var(--ink)">24/7</text>
        </svg>
        <span>618.472.9086</span>
      </div>
    </div>
  </section>
</body>
</html>
```